Warren D Pellham New Business Card Design

I assist families or individuals with downsizing. When they need to sell estate items I manage the process. I may buy their items. I may place their items with auction houses or I may bring in a variety of experts to sell all of the items. We help clients sell a huge variety of items including art, jewelry, coins, watches, antiques, collectibles, etc.

Target Market(s)

Two markets...One market is the clients I serve which are usually seniors or their family. These are individuals that need to sell on item or a house full if they estate is being liquidated. The other market is those that refer clients to me. Real Estate professionals, active senior communities, trust and estate lawyers and financial advisors.

Contact Information for Business Card

This is a new business so we do not have a logo. We may not need a logo. Feel free to visit our website at www.warrendpellham-example.com for more information on the service we provide. I am a private consultant so my name needs to be prominent. My name is my brand. We need the card to let people know how to contact us via phone, website and email. Easy to read. Many of our clients are elderly.

Font styles to use
Sans Serif

Requirements
Must have
• My name. Our contact information.
• Warren D Pellham
• 555-218-7034 Office
• 555-639-1582 Cell
• info@warrendpellham-example.com
• www.warrendpellham-example.com

```html
<!DOCTYPE html>
<html lang="en">
<head>
<meta charset="utf-8">
<title>Warren D Pellham – Business Card</title>
<link href="https://fonts.googleapis.com/css2?family=Raleway:wght@400;500;800&display=swap" rel="stylesheet">
<style>
  :root {
    --page-bg: #e6e8ea;
    --card-white: #ffffff;
    --panel-light: #f4fafd;
    --panel-mid: #c4e0ef;
    --brand-teal: #0b5f82;
    --text-teal: #0b5f82;
    --text-dark: #1c2a33;
  }
  html, body {
    margin: 0;
    width: 1200px;
    height: 900px;
    overflow: hidden;
    background: var(--page-bg);
  }
  .business-card {
    position: absolute;
    left: 75px;
    top: 150px;
    width: 1050px;
    height: 600px;
    box-shadow: 0 10px 30px rgba(0,0,0,0.18);
    background: var(--card-white);
    overflow: hidden;
  }
  .business-card svg { display: block; }
  .card-name {
    font-family: "Raleway", sans-serif;
    font-size: 44px;
    font-weight: 400;
    fill: var(--text-teal);
  }
  .card-name .surname { font-weight: 800; }
  .contact-line {
    font-family: "Raleway", sans-serif;
    font-size: 27px;
    font-weight: 500;
    fill: var(--text-dark);
  }
  .website-line {
    font-family: "Raleway", sans-serif;
    font-size: 33px;
    font-weight: 500;
    fill: var(--card-white);
  }
  .icon-badge { fill: var(--brand-teal); }
  .icon-glyph { fill: var(--card-white); }
  .icon-stroke { fill: none; stroke: var(--card-white); stroke-width: 2.2; }
</style>
</head>
<body>
  <div class="business-card">
    <svg width="1050" height="600" viewBox="0 0 1050 600">
      <defs>
        <radialGradient id="panelGradient" cx="0.7" cy="0.45" r="0.8">
          <stop offset="0" stop-color="#f4fafd"/>
          <stop offset="1" stop-color="#c4e0ef"/>
        </radialGradient>
        <linearGradient id="portraitGradient" x1="0" y1="0" x2="0" y2="1">
          <stop offset="0" stop-color="#7a6e66"/>
          <stop offset="0.3" stop-color="#3a3836"/>
          <stop offset="1" stop-color="#262626"/>
        </linearGradient>
      </defs>

      <rect class="portrait" role="img" aria-label="Portrait photo of Warren D Pellham in a dark suit, arms crossed"
            x="70" y="30" width="300" height="570" rx="6" fill="url(#portraitGradient)"/>

      <polygon class="contact-panel" points="528,0 1050,0 1050,600 360,600" fill="url(#panelGradient)"/>

      <polygon class="accent-stripe" points="488,0 530,0 494,130 452,130" fill="var(--brand-teal)"/>
      <rect class="name-underline" x="452" y="127" width="508" height="4" fill="var(--brand-teal)"/>

      <text class="card-name" x="540" y="112">Warren D. <tspan class="surname">PELLHAM</tspan></text>

      <circle class="icon-badge" cx="552" cy="225" r="15"/>
      <path class="icon-glyph" d="M544 216c2-2 4-2 5 0l2 3c1 1 0 3-1 4l-1 1c1 3 3 5 6 6l1-1c1-1 3-2 4-1l3 2c2 1 2 3 0 5l-2 1c-8 1-18-9-17-17z"/>
      <text class="contact-line" x="578" y="235">555-218-7034</text>

      <circle class="icon-badge" cx="552" cy="272" r="15"/>
      <rect class="icon-stroke" x="546" y="262" width="12" height="20" rx="2"/>
      <circle class="icon-glyph" cx="552" cy="278" r="1.5"/>
      <text class="contact-line" x="578" y="282">555-639-1582</text>

      <circle class="icon-badge" cx="552" cy="320" r="15"/>
      <rect class="icon-glyph" x="542" y="313" width="20" height="14" rx="1.5"/>
      <path d="M542 314l10 8 10-8" fill="none" stroke="var(--brand-teal)" stroke-width="2"/>
      <text class="contact-line" x="578" y="330">info@warrendpellham-example.com</text>

      <polygon class="website-band" points="412,410 1050,410 1050,525 380,525" fill="var(--brand-teal)"/>
      <circle class="icon-glyph" cx="452" cy="468" r="14"/>
      <g class="icon-globe" fill="none" stroke="var(--brand-teal)" stroke-width="2">
        <ellipse cx="452" cy="468" rx="5.5" ry="12"/>
        <line x1="440" y1="468" x2="464" y2="468"/>
      </g>
      <text class="website-line" x="476" y="480">www.warrendpellham-example.com</text>
    </svg>
  </div>
</body>
</html>
```